Vela Norvina is a dietary supplement company and in need of label design for 4 products

label for 4 dietary supplement products :1- Biotin. Red bottle ( please see the picture attached, not the whole bottle is colored but rather its a white bottle with the upper part and lower part of the bottle colored)2- COQ10. Orange Bottle 3- Hair Skin Nail. Pink bottle 4- Probiotics. Green Bottle we like the label to:1- have a modern and sleek appearance with very limited graphics.2- have a transparent background( as the bottle is white )3- have the box with the supplement and ingredient to appear sideways( horizontal )4- to have a color matching the bottle color.attached you will find :1- the dimension of the bottle.2- four different labels for each of the products.3- two pictures of the bottles 4- picture of the caps5- Logo
Industry/Entity Type
Health And Wellness
Colors
Designer to choose colors to be used in the design.
Look and feel
Each slider illustrates characteristics of the customer's brand and the style your logo design should communicate.

```html
<!DOCTYPE html>
<html lang="en">
<head>
<meta charset="utf-8">
<title>Vela Norvina – Hair, Skin &amp; Nails Essentials Label</title>
<link href="https://fonts.googleapis.com/css2?family=Open+Sans:wght@400;700&family=Montserrat:wght@800;900&family=Archivo+Black&family=Roboto+Condensed:wght@400;700&display=swap" rel="stylesheet">
<style>
  :root {
    --bg: #e4e4e6;
    --paper: #ffffff;
    --ink: #111111;
    --brand-pink: #c92a8f;
    --frame-grey: #58595b;
    --logo-ink: #3b4a3c;
  }
  * { box-sizing: border-box; margin: 0; padding: 0; }
  html, body { width: 1200px; height: 650px; overflow: hidden; background: var(--bg); }
  .label {
    position: absolute; left: 20px; top: 55px; width: 1160px; height: 540px;
    background: var(--paper); color: var(--ink);
    font-family: "Open Sans", Arial, sans-serif;
  }
  /* Left column: directions and warnings */
  .directions { position: absolute; left: 39px; top: 44px; width: 330px; font-size: 11.6px; line-height: 16px; }
  .directions p { margin-bottom: 16px; }
  .directions b { font-weight: 700; }
  .disclaimer {
    position: absolute; left: 34px; top: 380px; width: 303px; height: 81px;
    border: 2px solid var(--brand-pink); padding: 8px 12px 0 17px;
    font-size: 11.4px; line-height: 16px;
  }
  /* Centre column: brand and product name */
  .brand {
    position: absolute; left: 464px; top: 80px; width: 172px; text-align: center;
    font-family: "Open Sans", Arial, sans-serif; font-weight: 700; font-size: 24px;
    color: var(--logo-ink); letter-spacing: 0.5px;
  }
  .product-frame { position: absolute; left: 0; top: 0; width: 1160px; height: 540px; }
  .product-name {
    position: absolute; left: 458px; top: 178px;
    font-family: "Montserrat", Arial, sans-serif; font-weight: 900; color: var(--brand-pink);
    font-size: 68px; line-height: 62px; letter-spacing: -2px;
  }
  .product-sub {
    position: absolute; left: 460px; top: 380px;
    font-family: "Montserrat", Arial, sans-serif; font-weight: 800; color: var(--frame-grey);
    font-size: 34px; letter-spacing: -0.5px;
  }
  .capsule-count {
    position: absolute; left: 458px; top: 467px; background: var(--paper); padding-right: 6px;
    font-family: "Montserrat", Arial, sans-serif; font-weight: 800; color: var(--frame-grey);
    font-size: 19px; letter-spacing: -0.5px;
  }
  /* Right column: supplement facts */
  .facts {
    position: absolute; left: 800px; top: 49px; width: 248px; height: 445px;
    border: 2px solid var(--ink); padding: 6px 9px 0 10px;
    font-family: "Roboto Condensed", Arial, sans-serif;
  }
  .facts-title { font-family: "Archivo Black", Arial, sans-serif; font-size: 22.5px; line-height: 24px; letter-spacing: -0.3px; }
  .facts-serving { font-family: "Archivo Black", Arial, sans-serif; font-size: 6.5px; line-height: 9px; padding-left: 2px; }
  .facts-serving span { font-family: "Roboto Condensed", Arial, sans-serif; font-weight: 700; }
  .rule-thick { height: 6px; background: var(--ink); margin: 1px 0 4px; }
  .rule-mid { height: 3px; background: var(--ink); margin: 3px 0 2px; }
  .facts-head { font-size: 7.5px; font-weight: 700; text-align: right; padding-right: 27px; }
  .facts-head span { margin-left: 8px; }
  .facts-row {
    display: grid; grid-template-columns: 1fr 62px 34px;
    font-size: 9.8px; font-weight: 700; height: 17.3px; line-height: 16px;
    border-bottom: 1.3px solid var(--ink);
  }
  .facts-row .amt, .facts-row .dv { text-align: right; }
  .facts-row.last { border-bottom: 0; }
  .facts-blend { font-size: 9px; font-weight: 700; font-style: italic; line-height: 12.5px; padding: 3px 0 4px 4px; }
  .facts-foot { font-size: 10px; font-weight: 700; padding: 2px 0 0 4px; border-top: 5px solid var(--ink); margin-top: 1px; }
  /* Vertical side text */
  .side-text {
    position: absolute; writing-mode: vertical-rl; transform: rotate(180deg);
  }
  .inactive {
    left: 1055px; top: 56px; height: 428px; width: 32px;
    font-weight: 700; font-style: italic; font-size: 11px; line-height: 15px;
  }
  .distributor {
    left: 1099px; top: 280px; height: 204px; width: 34px;
    font-family: "Roboto Condensed", Arial, sans-serif; font-size: 9.3px; line-height: 11.5px;
  }
</style>
</head>
<body>
<main class="label">
  <section class="directions">
    <p><b>Suggested Use:</b> for adults only. Take two (2) capsules a day with food, DO not take this supplement within one hours of taking medication. Do not exceed the recommended dose.</p>
    <p><b>CAUTION:</b> Women who are preganate or lactating and anyone taking medications should consult a health care professional before using any nutritional product. if any adverse reactions occurm discontinue use and consult a health care professional.</p>
    <p><b>KEEP OUT THE REACH OF CHILDREN.<br>DO NOT USE IF SAFETY SEAL IS DAMAGED OR MISSING.<br>STRORE IN A COOL, DRY PLACE.</b></p>
    <p><b>IRON WARNING:</b> accidental overdose of &nbsp;iron-containint products is a leading cause of fatal poisoning in children under six (6) <b>KEEP OUT THE REACH OF CHILDRE.</b> In case of accidental overdose, call a doctor of poison control center immediately.</p>
  </section>
  <aside class="disclaimer">* These statement have not been evaluated by the food and drug administration. This products is not intended to diagnose, treat, cure or prevent any disease.</aside>

  <div class="brand">Vela Norvina</div>

  <svg class="product-frame" viewBox="0 0 1160 540" aria-hidden="true">
    <polyline points="636,210 700,210 700,447 461,447 461,430" fill="none" stroke="#58595b" stroke-width="4"/>
    <polyline points="461,476 461,461 700,461 700,490 600,490" fill="none" stroke="#58595b" stroke-width="4"/>
  </svg>
  <h1 class="product-name">HAIR,<br>SKIN &amp;<br>NAILS</h1>
  <div class="product-sub">ESSENTAILS</div>
  <div class="capsule-count">100 CAPSULES</div>

  <section class="facts">
    <div class="facts-title">Supplement Facts</div>
    <div class="facts-serving">Serving size: <span>2 Capsules</span></div>
    <div class="facts-serving">Servings Per Container: <span>Any Count</span></div>
    <div class="rule-thick"></div>
    <div class="facts-head">Amount Per Serving <span>%DV</span></div>
    <div class="rule-mid"></div>
    <div class="facts-row"><span>Vitamin A</span><span class="amt">2400 IU</span><span class="dv">40%</span></div>
    <div class="facts-row"><span>Vitamin C</span><span class="amt">120 mg</span><span class="dv">200%</span></div>
    <div class="facts-row"><span>Calcium Carbonate</span><span class="amt">80 mg</span><span class="dv">1%</span></div>
    <div class="facts-row"><span>Iron Ferrous Fumarate</span><span class="amt">14.5 mg</span><span class="dv">80%</span></div>
    <div class="facts-row"><span>Vitamin D3</span><span class="amt">800 IU</span><span class="dv">200%</span></div>
    <div class="facts-row"><span>Vitamin E</span><span class="amt">30 IU</span><span class="dv">100%</span></div>
    <div class="facts-row"><span>Vitamin B1</span><span class="amt">6 mg</span><span class="dv">400%</span></div>
    <div class="facts-row"><span>Vitamin B6</span><span class="amt">8 mg</span><span class="dv">400%</span></div>
    <div class="facts-row"><span>Folic Acid</span><span class="amt">880 ug</span><span class="dv">220%</span></div>
    <div class="facts-row"><span>Vitamin B12</span><span class="amt">12 ug</span><span class="dv">200%</span></div>
    <div class="facts-row"><span>Biotin</span><span class="amt">600 ug</span><span class="dv">200%</span></div>
    <div class="facts-row"><span>Vitamin B5</span><span class="amt">30 mg</span><span class="dv">300%</span></div>
    <div class="facts-row"><span>Magnesium Oxide</span><span class="amt">120 mg</span><span class="dv">30%</span></div>
    <div class="facts-row"><span>Zinc Oxide</span><span class="amt">7.2 mg</span><span class="dv">48%</span></div>
    <div class="facts-row"><span>Manganese Chelate</span><span class="amt">4 mg</span><span class="dv">200%</span></div>
    <div class="facts-row"><span>Potassium gluconate</span><span class="amt">12 mg</span><span class="dv">1%</span></div>
    <div class="facts-row last"><span>Proprietary Blend</span><span class="amt">409 mg</span><span class="dv">..</span></div>
    <div class="facts-blend">PABA, L-Tyrosine, Horsetail extract, Fo-Ti, Bamboo extract, nettle root, peony, Spirulina, Saw palmetto, Plant sterols, Alfalfa, Barley grass</div>
    <div class="facts-foot">** Daily Value (DV) Not Established</div>
  </section>

  <div class="side-text inactive">Inactive Ingredients: Cellulose (Vegetable Capsule), Rice Flour, Magnesium Stearate, Silicon Dioxide.</div>
  <div class="side-text distributor">DISTRIBUTED BY: COMPNAY NAME<br>STREET ADDRESS CITY STATE ZIPCODE<br>WEBSITE OR PHONE NUMBER</div>
</main>
</body>
</html>
```